Modern, upmarket label design for food product

We need a label design for a food company producing nuts with sesame and honey. In fact, we would like the words "Cashews med sesam & honning" on the label (It's in Danish and means - Cashews with sesame & honey). It should be easy for the customer to quickly understand what it is.

It is a shelf product in the competitive food industry, which is why the design should wake the feeling of 'just wanting to grab the product down from the shelves'. So, the design should stand out and have an image of a cool, modern, hip product. This being said, I love a raw & handmade look.

The company is called Pølle. Its origins are from the danish word Tiks that is a Danish slang for yummy. I have uploaded a photo of the package the products will be sold in.

Info & dimensions on bag in picture 1.
Dimensions: 6" x 9" | 15.2 cm x 22.3 cm
Capacity: 8 ounces | 250 grams (based on whole bean coffee)

Picture 2 is the same product, but has the possibility of attaching to a hanger on shelfs.

Picture 3 - I have also uploaded a photo of a product bag, where the hole is linear instead of a round hole. The designer chooses, which bag they will like to work with!

Please let me know if there are any questions!

Target Market(s)

Target market could really be any age, but the design needs to compel the target audience to pick it from the shelves. The package should signal a product you want to hold and have other people seeing you have it. The target audience is people who cares for what they buy, and typically doesn't want a low-end or budget product. They want the whole thing, meaning it has to taste good, look good etc. They are also the type of people who like to show off whatever products they buy by placing them in their houses for their guests to see. Or by uploading pictures of it on social medias.

Industry/Entity Type

It Company

Font styles to use
Other font styles liked:
• Not a must, but I like the 'Panton' script

Requirements
Must have
• My project must have the words 'Cashews med sesam & honning' on the label, so the customer will know within a second what they are looking at and buying.
Nice to have
• I am picturing the label with the words 'Cashews med sesam & honning' as a statement, again, emphasizing how the customer instantly should know what the product is. This being said, it should not be the only thing on the package and I love a raw & handmade look - which inspiration picture 5 is a great example of!
• I have uploaded photos of what I think looks good. With this said, I am not looking for a copy of those products, but see them as good inspiration. I have named the photos inspiration 1, 2, 3, 4 & 5.
• If needed, more text can be put on the label. For example 'vegan', 'laktosefri', Glutenfri', or 'Sund Snack' are great words for being used on the label.
Should not have
• The fonts on the label should not be too decorative. Personally I like an easy too read font.

```html
<!DOCTYPE html>
<html lang="da">
<head>
<meta charset="utf-8">
<title>Cashews med sesam &amp; honning – label</title>
<link href="https://fonts.googleapis.com/css2?family=Alfa+Slab+One&family=Josefin+Sans:wght@700&display=swap" rel="stylesheet">
<style>
  :root {
    --paper: #f1eadf;
    --paper-edge: #e4d8c6;
    --ink: #4a3226;
    --label-green: #a6cb3a;
    --page: #ffffff;
  }
  * { margin: 0; padding: 0; box-sizing: border-box; }
  html, body { width: 705px; height: 1200px; overflow: hidden; background: var(--page); }
  .canvas { position: relative; width: 705px; height: 1200px; }

  /* Statement panel */
  .statement {
    position: absolute; left: 0; top: 0; width: 705px; height: 553px;
    background: radial-gradient(ellipse at 50% 45%, var(--paper) 55%, var(--paper-edge) 100%);
    overflow: hidden;
  }
  .brand {
    display: inline-flex; align-items: center; gap: 8px;
    font-family: "Alfa Slab One", serif; color: var(--ink); line-height: 1;
  }
  .brand-square { display: inline-block; background: var(--ink); }
  .statement-brand {
    position: absolute; left: 260px; top: 122px;
    transform: translate(-50%, -50%);
    font-size: 40px;
  }
  .statement-brand .brand-square { width: 20px; height: 20px; }
  .statement-title {
    position: absolute; left: 349px; top: 330px; width: 500px;
    transform: translate(-50%, -50%) rotate(-24deg);
    color: var(--ink); line-height: 1; text-align: left; font-weight: normal;
  }
  .statement-title .product {
    display: block;
    font-family: "Alfa Slab One", serif; font-size: 84px; letter-spacing: 1px;
  }
  .statement-title .flavour {
    display: block;
    font-family: "Josefin Sans", sans-serif; font-weight: 700; font-size: 68px;
    letter-spacing: 3px; margin-top: 14px; white-space: nowrap;
  }
  .statement-title .flavour + .flavour { margin-top: 12px; }

  /* Bag label */
  .label {
    position: absolute; left: 233px; top: 578px; width: 210px; height: 343px;
    background: var(--label-green);
    border-radius: 0 0 105px 105px;
    color: var(--ink); text-align: center;
  }
  .label-brand {
    position: absolute; left: 50%; top: 32px; transform: translateX(-50%);
    font-size: 22px; gap: 5px;
  }
  .label-brand .brand-square { width: 10px; height: 10px; }
  .label-title {
    position: absolute; left: 0; top: 86px; width: 100%;
    line-height: 1.05; font-weight: normal;
  }
  .label-title .product { display: block; font-family: "Alfa Slab One", serif; font-size: 28px; letter-spacing: 1px; }
  .label-title .flavour { display: block; font-family: "Josefin Sans", sans-serif; font-weight: 700; font-size: 24px; letter-spacing: 1px; margin-top: 3px; white-space: nowrap; }
  .badges {
    position: absolute; left: 0; top: 196px; width: 100%;
    display: flex; justify-content: center; gap: 24px;
  }
  .badge { width: 40px; height: 40px; border: 2px solid var(--ink); border-radius: 5px; }
  .label-brand-small {
    position: absolute; left: 50%; top: 256px; transform: translateX(-50%);
    font-size: 18px; gap: 4px;
  }
  .label-brand-small .brand-square { width: 8px; height: 8px; }
  .label-arc { position: absolute; left: 0; bottom: 0; width: 210px; height: 100px; }
  .label-arc text {
    font-family: "Alfa Slab One", serif; font-size: 17px; fill: var(--ink); letter-spacing: 1px;
  }
</style>
</head>
<body>
<div class="canvas">
  <section class="statement">
    <div class="brand statement-brand"><span class="brand-square"></span>Pølle</div>
    <h1 class="statement-title">
      <span class="product">CASHEWS</span>
      <span class="flavour">MED SESAM</span>
      <span class="flavour">&amp; HONNING</span>
    </h1>
  </section>

  <section class="label">
    <div class="brand label-brand"><span class="brand-square"></span>Pølle</div>
    <h2 class="label-title">
      <span class="product">CASHEWS</span>
      <span class="flavour">MED SESAM</span>
      <span class="flavour">&amp; HONNING</span>
    </h2>
    <div class="badges">
      <span class="badge" aria-label="Glutenfri"></span>
      <span class="badge" aria-label="Laktosefri"></span>
      <span class="badge" aria-label="Vegansk"></span>
    </div>
    <div class="brand label-brand-small"><span class="brand-square"></span>Pølle</div>
    <svg class="label-arc" viewBox="0 0 210 100" aria-label="Sund snack">
      <defs>
        <path id="snack-curve" d="M 30 28 Q 105 100 180 28"/>
      </defs>
      <text text-anchor="middle"><textPath href="#snack-curve" startOffset="50%">SUND SNACK</textPath></text>
    </svg>
  </section>
</div>
</body>
</html>
```